Energy trading company (Voltrisa) needs a business card

We need a business card for a company based in Central America. Our main purpose is trading energy . We already have the logo but we need some good creativity to design a high impact business card. Colors blue, orange, green can be used or we would like to see good combinatios with our logo

Target Market(s)

Energy

Industry/Entity Type

Power Generation

Contact Information for Business Card

Logo , headquarters , name, background

Font styles to use
Serif
Sans Serif

Colors

Designer to choose colors to be used in the design.

Requirements
Must have
• it must have a fresh and clean view
Nice to have
• good backgrounds that combine with the logo
Should not have
• too much words

```html
<!DOCTYPE html>
<html lang="en">
<head>
<meta charset="utf-8">
<title>Voltrisa Business Card</title>
<link rel="stylesheet" href="https://fonts.googleapis.com/css2?family=Lato:wght@400;700&family=Arimo:wght@400;700&display=swap">
<style>
  :root {
    --stage: #1c1c1e;
    --card: #232325;
    --card-edge: #2c2c2e;
    --ink-silver: #8e8e92;
    --ink-light: #b4b4b8;
    --ink-soft: #9a9a9e;
    --rule: #6e6e72;
  }
  * { margin: 0; padding: 0; box-sizing: border-box; }
  html, body {
    width: 1200px;
    height: 900px;
    overflow: hidden;
    background: var(--stage);
  }
  .canvas {
    width: 1200px;
    height: 900px;
    display: flex;
    flex-direction: column;
    align-items: center;
    justify-content: center;
    gap: 48px;
  }
  .card {
    width: 700px;
    height: 400px;
    background: var(--card);
    border: 1px solid var(--card-edge);
    position: relative;
  }
  .card-front {
    display: flex;
    flex-direction: column;
    align-items: center;
    justify-content: center;
    gap: 22px;
  }
  .brand-dot {
    width: 64px;
    height: 64px;
    border-radius: 50%;
    background: var(--ink-silver);
  }
  .brand-name {
    font-family: "Lato", sans-serif;
    font-weight: 400;
    color: var(--ink-silver);
    letter-spacing: 2px;
    text-transform: uppercase;
    line-height: 1;
  }
  .card-front .brand-name { font-size: 78px; }

  .card-back {
    display: flex;
    align-items: center;
    padding: 0 56px;
  }
  .back-brand {
    width: 300px;
    display: flex;
    flex-direction: column;
    align-items: center;
    gap: 16px;
  }
  .back-brand .brand-dot { width: 46px; height: 46px; }
  .back-brand .brand-name { font-size: 50px; }
  .divider {
    width: 1px;
    height: 200px;
    background: var(--rule);
    margin: 0 32px 0 24px;
  }
  .contact {
    font-family: "Arimo", sans-serif;
    color: var(--ink-soft);
  }
  .person-name {
    font-weight: 700;
    font-size: 24px;
    letter-spacing: 1.5px;
    color: var(--ink-light);
    text-transform: uppercase;
  }
  .person-role { font-size: 15px; margin-bottom: 20px; }
  .address { font-size: 16px; line-height: 1.3; margin-bottom: 18px; max-width: 280px; }
  .contact-list { list-style: none; font-size: 17px; }
  .contact-list li {
    display: flex;
    align-items: center;
    gap: 14px;
    margin-bottom: 6px;
  }
  .contact-icon { width: 16px; height: 16px; flex: none; }
</style>
</head>
<body>
<main class="canvas">
  <section class="card card-front" aria-label="Card front">
    <span class="brand-dot" aria-hidden="true"></span>
    <span class="brand-name">Voltrisa</span>
  </section>

  <section class="card card-back" aria-label="Card back">
    <div class="back-brand">
      <span class="brand-dot" aria-hidden="true"></span>
      <span class="brand-name">Voltrisa</span>
    </div>
    <span class="divider" aria-hidden="true"></span>
    <div class="contact">
      <p class="person-name">Marco Delrey</p>
      <p class="person-role">President</p>
      <p class="address">00000 Paseo Norte Ofc 48, Central America, PN 00000</p>
      <ul class="contact-list">
        <li>
          <svg class="contact-icon" viewBox="0 0 16 16" aria-hidden="true"><path d="M3 1.5l2.5 0 1 3.5-1.6 1.2a9 9 0 0 0 4.9 4.9L11 9.5l3.5 1v2.5c0 .8-.7 1.5-1.5 1.5A11.5 11.5 0 0 1 1.5 3c0-.8.7-1.5 1.5-1.5z" fill="none" stroke="#9a9a9e" stroke-width="1.2"/></svg>
          <span>+00 000 000 000</span>
        </li>
        <li>
          <svg class="contact-icon" viewBox="0 0 16 16" aria-hidden="true"><rect x="1" y="3" width="14" height="10" fill="none" stroke="#9a9a9e" stroke-width="1.2"/><path d="M1 3l7 6 7-6" fill="none" stroke="#9a9a9e" stroke-width="1.2"/></svg>
          <span>info@voltrisa.com</span>
        </li>
        <li>
          <svg class="contact-icon" viewBox="0 0 16 16" aria-hidden="true"><circle cx="8" cy="8" r="6.5" fill="none" stroke="#9a9a9e" stroke-width="1.2"/><ellipse cx="8" cy="8" rx="3" ry="6.5" fill="none" stroke="#9a9a9e" stroke-width="1.2"/><path d="M1.5 8h13" stroke="#9a9a9e" stroke-width="1.2"/></svg>
          <span>www.voltrisa.com</span>
        </li>
      </ul>
    </div>
  </section>
</main>
</body>
</html>
```